Stationary for a Legal Support Company
Brimvale Courier & Records, Inc.
Stationary for a Legal Support Company - Marketing
Creative Brief
Professional
Rupert J Olwen
PO Box 712 4175 Marrow Ln Halbrook OH 44291
tkorvel@brimcr.com
www.brimcr.com
Generic USB flash and CD/DVD layout also appreciated.
Back of the card can include the logo or logo/text.
tkorvel tkorvel
Thank you all for your submissions. I believe I have sent some comments to everyone who has entered a submission. If you did not receive a comment from me, please let me know.

```html
<!DOCTYPE html>
<html lang="en">
<head>
<meta charset="utf-8">
<title>Brimvale Courier &amp; Records — Business Card</title>
<link rel="stylesheet" href="https://fonts.googleapis.com/css2?family=Open+Sans:ital,wght@0,400;0,600;1,400&display=swap">
<style>
  :root {
    --brand-blue: #1d4f9c;
    --brand-blue-dark: #163f80;
    --accent-gray: #5b5f66;
    --ink: #3a3d42;
    --paper: #ffffff;
    --backdrop: #e9eaec;
  }
  * { margin: 0; padding: 0; box-sizing: border-box; }
  html, body {
    width: 1200px; height: 901px; overflow: hidden;
    background: var(--backdrop);
    font-family: "Open Sans", Arial, sans-serif;
  }
  .canvas { position: relative; width: 1200px; height: 901px; }

  .card {
    position: absolute;
    border-radius: 4px;
    overflow: hidden;
    box-shadow: 0 10px 28px rgba(0,0,0,0.18);
  }

  /* Back of card */
  .card-back {
    left: 100px; top: 70px; width: 600px; height: 343px;
    background: linear-gradient(135deg, var(--brand-blue) 0%, var(--brand-blue-dark) 100%);
    display: flex; align-items: center; justify-content: center;
  }
  .back-wordmark {
    display: flex; align-items: center; gap: 14px;
    color: var(--paper);
    font-weight: 600; font-size: 24px; letter-spacing: 0.5px;
  }
  .wordmark-dot {
    width: 26px; height: 26px; border-radius: 50%;
    border: 2px solid var(--paper);
  }

  /* Front of card */
  .card-front {
    left: 460px; top: 470px; width: 640px; height: 366px;
    background: var(--paper);
  }
  .front-sweep { position: absolute; inset: 0; }
  .front-wordmark {
    position: absolute; left: 34px; top: 56px;
    display: flex; align-items: center; gap: 10px;
    color: var(--brand-blue);
    font-weight: 600; font-size: 18px; line-height: 1.2;
    width: 240px;
  }
  .front-wordmark .wordmark-dot {
    flex: none; width: 22px; height: 22px;
    border-color: var(--brand-blue);
  }
  .holder-name {
    position: absolute; right: 40px; top: 92px;
    color: var(--paper);
    font-weight: 600; font-size: 17px; letter-spacing: 0.4px;
  }
  .mailing-address {
    position: absolute; left: 34px; top: 196px;
    font-style: italic; font-size: 13.5px; line-height: 1.35;
    color: var(--ink);
  }
  .contact-list {
    position: absolute; right: 34px; bottom: 28px;
    list-style: none;
    font-size: 14px; line-height: 1.5; color: var(--ink);
  }
  .contact-list li { display: flex; align-items: center; gap: 9px; }
  .contact-icon { width: 13px; height: 13px; flex: none; }
</style>
</head>
<body>
<main class="canvas">

  <section class="card card-back" aria-label="Card back">
    <div class="back-wordmark">
      <span class="wordmark-dot"></span>
      <span>Brimvale Courier &amp; Records</span>
    </div>
  </section>

  <section class="card card-front" aria-label="Card front">
    <svg class="front-sweep" viewBox="0 0 640 366" width="640" height="366" aria-hidden="true">
      <path d="M286 0 C420 70 560 170 640 300 V0 Z" fill="var(--accent-gray)"/>
      <path d="M300 0 C430 60 560 150 640 268 V0 Z" fill="var(--brand-blue)"/>
    </svg>

    <div class="front-wordmark">
      <span class="wordmark-dot"></span>
      <span>Brimvale Courier &amp; Records</span>
    </div>

    <p class="holder-name">Rupert J Olwen</p>

    <address class="mailing-address">
      PO Box 712<br>
      4175 Marrow Ln<br>
      Halbrook OH 44291
    </address>

    <ul class="contact-list">
      <li>
        <svg class="contact-icon" viewBox="0 0 16 16" aria-hidden="true">
          <path d="M3 1 L6 1 L7 5 L5 6.5 C6 9 7 10 9.5 11 L11 9 L15 10 L15 13 C15 14 14 15 13 15 C6.5 14.5 1.5 9.5 1 3 C1 2 2 1 3 1 Z" fill="var(--brand-blue)"/>
        </svg>
        (330) 555-0148
      </li>
      <li>
        <svg class="contact-icon" viewBox="0 0 16 16" aria-hidden="true">
          <rect x="1" y="3" width="14" height="10" rx="1" fill="var(--brand-blue)"/>
          <path d="M1.5 3.8 L8 9 L14.5 3.8" fill="none" stroke="#fff" stroke-width="1.2"/>
        </svg>
        tkorvel@brimcr.com
      </li>
      <li>
        <svg class="contact-icon" viewBox="0 0 16 16" aria-hidden="true">
          <circle cx="8" cy="8" r="7" fill="var(--brand-blue)"/>
          <path d="M1 8 H15 M8 1 C5 4 5 12 8 15 M8 1 C11 4 11 12 8 15" fill="none" stroke="#fff" stroke-width="1"/>
        </svg>
        www.brimcr.com
      </li>
    </ul>
  </section>

</main>
</body>
</html>
```